Quorvane - corporate Business Card

We need a good look and innovative business card for a new start up company based in Los Angeles called "Quorvane". We are in a payment business, including payment card, app, and ewallet. We are expert in online payment and Card not present (CNP) transaction.
We need an innovative, modern business card.

Our logo font is Aero Matics

Target Market(s)

Startup - Bank - Online Payment - Card Manufacturing

Industry/Entity Type

Startup

Contact Information for Business Card

phone: 424 555 0173 - Address: 4270 Marbrook blvd, Dellmere, CA 90418

Requirements
Must have
• Message: innovative, professional, expert, high tech, trust, online payment expert, security
Nice to have
• no comment
Should not have
• no Comment

```html
<!DOCTYPE html>
<html lang="en">
<head>
<meta charset="utf-8">
<title>Quorvane — Business Card</title>
<link href="https://fonts.googleapis.com/css2?family=Saira:wght@400;500;600;700&display=swap" rel="stylesheet">
<style>
  :root {
    --brand-red: #b01c2e;
    --card-white: #f7f7f5;
    --ink: #2b2b2b;
    --ink-soft: #555;
    --rule: #a9a9a9;
    --backdrop: #e9e6e1;
  }
  * { box-sizing: border-box; margin: 0; padding: 0; }
  html, body { width: 1200px; height: 769px; overflow: hidden; }
  body {
    background: var(--backdrop);
    font-family: "Saira", sans-serif;
    position: relative;
  }
  .card {
    position: absolute;
    width: 460px;
    height: 263px;
    border-radius: 18px;
    box-shadow: 0 10px 28px rgba(0,0,0,0.18);
  }
  .card-front {
    left: 95px; top: 253px;
    background: var(--brand-red);
    color: #fff;
  }
  .brand {
    position: absolute;
    left: 0; right: 0; top: 92px;
    display: flex; align-items: center; justify-content: center;
    gap: 10px;
  }
  .brand-dot {
    width: 50px; height: 50px; border-radius: 50%;
    background: #fff;
  }
  .brand-name {
    font-size: 42px; font-weight: 600; letter-spacing: 0.5px;
    line-height: 1; color: #fff;
  }
  .tagline {
    position: absolute;
    left: 26px; right: 26px; bottom: 22px;
    font-size: 8.5px; letter-spacing: 0.3px;
    display: flex; justify-content: space-between; white-space: nowrap;
  }
  .card-back {
    left: 645px; top: 253px;
    background: var(--card-white);
    color: var(--ink);
    text-align: center;
  }
  .person-name {
    margin-top: 40px;
    font-size: 17px; font-weight: 600; letter-spacing: 1px;
  }
  .person-role { font-size: 9px; color: var(--ink-soft); margin-top: -2px; }
  .contact-list { list-style: none; margin: 10px 60px 0; }
  .contact-list li {
    border-top: 1px solid var(--rule);
    padding: 8px 0 6px;
    font-size: 9.5px; font-weight: 500; letter-spacing: 0.6px;
  }
  .contact-list li:last-child { border-bottom: 1px solid var(--rule); }
  .website { margin-top: 12px; font-size: 9.5px; font-weight: 600; letter-spacing: 0.4px; }
  .mini-dot {
    width: 22px; height: 22px; border-radius: 50%;
    background: var(--brand-red);
    margin: 12px auto 0;
  }
</style>
</head>
<body>
  <section class="card card-front" aria-label="Card front">
    <div class="brand">
      <span class="brand-dot"></span>
      <span class="brand-name">quorvane</span>
    </div>
    <p class="tagline">
      <span>innovative</span><span>•</span><span>professional</span><span>•</span><span>expert</span><span>•</span><span>high tech</span><span>•</span><span>trust</span><span>•</span><span>online payment expert</span><span>•</span><span>security</span>
    </p>
  </section>

  <section class="card card-back" aria-label="Card back">
    <h1 class="person-name">DANA WHITFIELD</h1>
    <p class="person-role">President</p>
    <ul class="contact-list">
      <li>424 555 0173</li>
      <li>4270 Marbrook blvd, Dellmere, CA 90418</li>
    </ul>
    <p class="website">www.quorvanepay.com</p>
    <div class="mini-dot"></div>
  </section>
</body>
</html>
```